Tri-Fold Menu of Services for our Eyelash and Skin Care Spa

We need a beautiful spa service menu for our upscale spa in St. Charles Missouri. We specialize in providing treatments that are specific to the clients needs. Our services are eyelash extensions, skin care treatments, full body waxing and makeup application. Our spa colors are dark purples and greys and we are not opposed to additional colors that would complement those colors. We do a lot of eyelash extensions and while we do what those services listed we would like the skin care treatments to be in an area that would be noticed first. One of the attachments lists all of our services, descriptions and prices (please be sure to include all services and pricing. descriptions if possible). And our website has more information about us if needed. The website was not professionally done. So it DOESN'T represent our style exactly.

I HAVE ATTACHED A FEW PHOTOS BUT THEY DON'T HAVE TO BE USED.

Target Market(s)

women who would like to look their best, 35-55, annual income of 100,000+, she is usually busy and her children (if she has any) are high school age or older.

Industry/Entity Type

It Service

Font styles to use
Serif
Sans Serif

Requirements
Must have
• Must list all of our services. If it works to have the descriptions that would be great.
Nice to have
• If it works to have the descriptions of each service that would be great.

```html
<!DOCTYPE html>
<html lang="en">
<head>
<meta charset="utf-8">
<title>Lumelle Lash &amp; Skin Studio — Service Menu</title>
<link href="https://fonts.googleapis.com/css2?family=Cormorant+Garamond:wght@500;600&family=Roboto+Condensed:wght@400;700&family=Roboto:wght@400;700&display=swap" rel="stylesheet">
<style>
  :root{
    --plum-deep:#3b1242;
    --plum:#5e2468;
    --violet:#8a4a9c;
    --orchid:#b785c4;
    --lilac:#d9bfe0;
    --blush-label:#c58fcd;
    --ink:#2e2e2e;
    --paper:#ffffff;
    --stage:#e6e6e6;
    --serif:"Cormorant Garamond", Georgia, serif;
    --sans:"Roboto Condensed", "Arial Narrow", sans-serif;
    --sans-wide:"Roboto", Arial, sans-serif;
  }
  *{box-sizing:border-box;margin:0;padding:0}
  html,body{width:1200px;height:1085px;overflow:hidden;background:var(--stage)}
  .canvas{position:relative;width:1200px;height:1085px}
  .spread{position:absolute;left:260px;width:680px;height:525px;background:var(--paper);overflow:hidden}
  .spread--outside{top:14px}
  .spread--inside{top:556px}

  /* ---------- outside spread ---------- */
  .hero-art{position:absolute;left:0;top:0;width:680px;height:360px}
  .services-intro{position:absolute;left:0;width:228px;top:274px;text-align:center;color:var(--ink)}
  .services-intro h2{font-family:var(--serif);font-weight:500;font-size:14.5px;letter-spacing:.3px;color:var(--plum-deep)}
  .services-intro p{font-family:var(--sans-wide);font-size:7.2px;line-height:10px;letter-spacing:.2px}
  .spa-photo{position:absolute;left:0;top:310px;width:228px;height:215px;
    background:linear-gradient(160deg,#efe4ea 0%,#e2cbd4 45%,#f6f1f3 100%)}
  .panel-fade{position:absolute;top:340px;height:185px;
    background:linear-gradient(180deg,#ffffff 0%,#f4f0f5 100%)}
  .panel-fade--middle{left:228px;width:225px}
  .panel-fade--right{left:453px;width:227px;background:#fff}
  .visit{position:absolute;left:262px;top:354px;font-family:var(--sans);color:var(--ink)}
  .label{font-family:var(--sans);font-weight:700;font-size:9.5px;letter-spacing:1.6px;color:var(--blush-label)}
  .address{font-size:8.6px;line-height:12px;margin-top:2px;font-family:var(--sans-wide)}
  .hours{position:absolute;left:262px;top:403px}
  .hours dl{display:grid;grid-template-columns:62px 60px;margin:3px 0 0 30px;font-family:var(--sans-wide);font-size:8px;line-height:11.3px;color:var(--ink)}
  .brand{position:absolute;left:453px;width:227px;top:412px;text-align:center;color:var(--plum-deep);font-family:var(--serif);font-weight:600}
  .brand__name{font-size:40px;line-height:38px;display:flex;align-items:center;justify-content:center;gap:8px}
  .brand__mark{width:10px;height:10px;border-radius:50%;background:var(--plum-deep)}
  .brand__tag{font-size:12px;letter-spacing:.5px}
  .call{position:absolute;left:453px;width:227px;top:492px;text-align:center;font-family:var(--sans-wide);font-size:10.6px;letter-spacing:2.4px;color:var(--plum-deep)}
  .call strong{font-weight:700;letter-spacing:1.8px}

  /* ---------- inside spread ---------- */
  .treatments{position:absolute;left:0;top:0;width:453px;height:525px;color:#fff;
    background:radial-gradient(ellipse at 70% 40%,#d8b6df 0%,rgba(216,182,223,0) 55%),
               linear-gradient(100deg,#7f3f92 0%,#9c5fae 40%,#c59bcf 75%,#b27fc0 100%)}
  .treatments h1{position:absolute;left:16px;top:10px;font-family:var(--serif);font-weight:500;font-size:17.5px;letter-spacing:.8px}
  .treatment{position:absolute;left:35px;width:380px}
  .treatment__head{display:grid;grid-template-columns:259px 32px 1fr;font-family:var(--sans);font-weight:700;font-size:8.4px;line-height:9px;text-transform:uppercase}
  .treatment p{font-family:var(--sans-wide);font-size:7.9px;line-height:7.8px}
  .note{position:absolute;left:35px;top:319px;font-family:var(--sans-wide);font-size:7.9px}
  .peels{position:absolute;left:35px;top:393px;width:215px;font-family:var(--sans-wide)}
  .addons{position:absolute;left:252px;top:393px;width:182px;font-family:var(--sans-wide)}
  .peels h3,.addons h3{font-family:var(--sans);font-size:10.5px;font-weight:700;line-height:12px}
  .peel{display:grid;grid-template-columns:80px 66px 1fr;font-size:8px;line-height:10.2px;white-space:nowrap}
  .peel b{font-family:var(--sans);font-weight:700;font-size:8.2px}
  .peel-note{font-family:var(--sans);font-size:6.2px;font-weight:700;line-height:10.2px;padding-left:4px;text-transform:uppercase}
  .peel-foot{font-size:6.4px;line-height:9px;padding-left:4px}
  .addon{display:flex;justify-content:space-between;font-size:8px;line-height:10.3px}
  .addon b{font-family:var(--sans);font-weight:700}
  .addon--sub{padding-left:4px;justify-content:flex-start}
  .addon--sub span:first-child{width:112px}

  .rates{position:absolute;left:453px;top:0;width:227px;height:525px;background:var(--paper);color:var(--ink);font-family:var(--sans-wide)}
  .rates h2{position:absolute;left:16px;font-family:var(--serif);font-weight:500;font-size:16.5px;color:#222}
  .rates .label{position:absolute;left:27px;font-size:9.5px;letter-spacing:.6px}
  .rate{position:absolute;left:47px;display:grid;grid-template-columns:62px 1fr;font-size:8px;line-height:8.5px}
  .lash-photo{position:absolute;left:139px;width:76px;height:26px;
    background:linear-gradient(90deg,#6b5a55 0%,#d9c4bb 40%,#efe0d8 70%,#7a6660 100%)}
  .massage{position:absolute;left:27px;font-size:8px;line-height:8.5px}
  .massage span{display:grid;grid-template-columns:62px 1fr;padding-left:20px}
  .massage-note{position:absolute;left:27px;top:404px;width:170px;font-size:8px;line-height:8.6px}
  .massage-photo{position:absolute;left:0;top:440px;width:227px;height:85px;
    background:linear-gradient(180deg,#ffffff 0%,#f0e6ee 60%,#e6d6e2 100%)}
</style>
</head>
<body>
<div class="canvas">

  <section class="spread spread--outside" aria-label="Brochure outside">
    <div class="panel-fade panel-fade--middle"></div>
    <div class="panel-fade panel-fade--right"></div>

    <svg class="hero-art" viewBox="0 0 680 360" role="img" aria-label="Photo of a woman with eyes closed having powder applied with a makeup brush on a soft violet background">
      <defs>
        <linearGradient id="heroFill" x1="0" y1="0" x2="1" y2="0.6">
          <stop offset="0" stop-color="#8c4b9e"/>
          <stop offset="0.45" stop-color="#c9a3d2"/>
          <stop offset="0.75" stop-color="#f1e3ea"/>
          <stop offset="1" stop-color="#b887c4"/>
        </linearGradient>
        <linearGradient id="swoosh" x1="0" y1="0" x2="1" y2="0">
          <stop offset="0" stop-color="#3b1242"/>
          <stop offset="0.5" stop-color="#6d3579"/>
          <stop offset="1" stop-color="#b98cc6"/>
        </linearGradient>
      </defs>
      <path d="M0 0 H680 V330 C430 345 200 250 0 110 Z" fill="url(#heroFill)"/>
      <path d="M0 110 C200 250 430 345 680 330 V354 C420 365 190 270 0 124 Z" fill="url(#swoosh)"/>
    </svg>

    <div class="services-intro">
      <h2>OUR SERVICES INCLUDE</h2>
      <p>EYELASH EXTENSIONS | SKIN CARE TREATMENTS<br>FULL BODY WAXING | MAKEUP APPLICATION</p>
    </div>

    <div class="spa-photo" role="img" aria-label="Photo of a relaxed woman receiving a facial massage"></div>

    <div class="visit">
      <div class="label">LOCATED</div>
      <p class="address">2480 Larkspur Ln<br>Fernhill, MO 63390</p>
    </div>

    <div class="hours">
      <div class="label">STORE HOURS</div>
      <dl>
        <dt>Saturday</dt><dd>9AM–3PM</dd>
        <dt>Sunday</dt><dd>Closed</dd>
        <dt>Monday</dt><dd>10AM–2PM</dd>
        <dt>Tuesday</dt><dd>10AM–8PM</dd>
        <dt>Wednesday</dt><dd>10AM–8PM</dd>
        <dt>Thursday</dt><dd>11AM–8PM</dd>
        <dt>Friday</dt><dd>10AM–6PM</dd>
      </dl>
    </div>

    <div class="brand">
      <div class="brand__name"><span class="brand__mark"></span>Lumelle</div>
      <div class="brand__tag">Lash &amp; Skin Studio</div>
    </div>
    <p class="call">CALL US <strong>636-555-0192</strong></p>
  </section>

  <section class="spread spread--inside" aria-label="Brochure inside">
    <div class="treatments">
      <h1>FACIAL &amp; SKIN TREATMENTS</h1>

      <article class="treatment" style="top:41px">
        <div class="treatment__head"><span>Essential Deep Cleansing Treatment</span><span>$65</span><span>60 Minutes</span></div>
        <p>This relaxing, purifying treatment consists of steaming, exfoliation, and an intense deeper cleansing of clogged pores. A skintype specific ampoule is gently massaged into the skin of your face, neck, and decollete, followed by a therapist selected mask. Beneficial for all skin types.</p>
      </article>

      <article class="treatment" style="top:87px">
        <div class="treatment__head"><span>Mini Facial</span><span>$48</span><span>30 Minutes</span></div>
        <p>This express facial is ideal for those on the go. Your skin is cleansed, lightly exfoliated and gently massaged. A porerefining mask is then applied, followed by a veil of light moisturizer.</p>
      </article>

      <article class="treatment" style="top:118px">
        <div class="treatment__head"><span>Aromatherapy Facial</span><span>$75</span><span>60 Minutes</span></div>
        <p>Our Aromatherapy facial will naturally enhance the facial benefits using fragrant oils extracted from flowers, fruits and herbs.</p>
      </article>

      <article class="treatment" style="top:149px">
        <div class="treatment__head"><span>Radiant Lift &amp; Glow Treatment Facial</span><span>$95</span><span>60 Minutes</span></div>
        <p>Seeking a treatment with amazing instant results? Redefining radiance and facial contouring, this exclusively formulated treatment features the latest in freezedried technology to deliver instant results and cumulative skin care benefits. Ideal for any skin type showing signs of aging, or as the perfect instant repair boost when you want to look your best. Proven to perform, the Verelle Radiant Lift &amp; Glow facial renders your skin ultraluminous with a firmer, tighter, and more youthfully defined appearance.</p>
      </article>

      <article class="treatment" style="top:211px">
        <div class="treatment__head"><span>Soothing Botanical Calm Facial</span><span>$100</span><span>60 Minutes</span></div>
        <p>This highly effective, soothing treatment calms redness and alleviates irritated or sensitive skin. A healing Propolis ampoule (natural ingredient collected by bees) is applied to desensitize the skin's surface and strengthen capillaries. A cooling liftoff mask is then applied to seal in the vitamin enriched beneficial ampoule.</p>
      </article>

      <article class="treatment" style="top:257px">
        <div class="treatment__head"><span>Radiance Phototherapy Treatment</span><span>$150</span><span>Package 8/$800</span></div>
        <p>Uses heat and light energy to gently break up areas of excess pigment while stimulating the production of new collagen. Improved skin tone, less spots, fewer pink areas, less redness, reduction in fine lines and wrinkles. Diminishes pores and restores natural radiant glow of skin. Like laser treatments MicroPhotoTherapy treats skin with therapeutic light energy but unlike laser treatments, Micro PhotoTherapy features gentle waves of heat and light that improve the skin with no downtime and very little discomfort.</p>
      </article>

      <p class="note">We recommend 8 treatments 1 to 2 times a week for best results.</p>

      <article class="treatment" style="top:334px">
        <div class="treatment__head"><span>Diamond Microdermabrasion Treatment</span><span>$78</span><span></span></div>
        <p>With this treatment you will see softening of fine lines and wrinkles and smoothing of coarsely textured skin. Dull, stressed or congested skin will be brighter and clearer. The appearance of enlarged pores, and acne scars will be minimized. Your at home products will be able to penetrate deeper therefore, are more effective. Or add this to any facial or most peels for just $30.</p>
      </article>

      <div class="peels">
        <h3>PEELS</h3>
        <div class="peel"><span>Clear Skin Peel</span><b>$50/1 $250/6</b><b>30 MINUTES</b></div>
        <div class="peel-note">Mild to moderate acne peel</div>
        <div class="peel"><span>Brightening Peel</span><b>$50/1 $250/6</b><b>30 MINUTES</b></div>
        <div class="peel-note">Pigmentation (sun/brown spots), uneven skin tone</div>
        <div class="peel"><span>Smoothing Peel</span><b>$50/1 $250/6</b><b>30 MINUTES</b></div>
        <div class="peel-note">Aging, fine lines and wrinkles</div>
        <div class="peel"><span>Calming Peel</span><b>$50/1 $250/6</b><b>30 MINUTES</b></div>
        <div class="peel-note">Rosacea, dry/dehydrated</div>
        <div class="peel"><span>Renewal Peel</span><b>$100/1 $350/4</b><b>30 MINUTES</b></div>
        <div class="peel-note">Advanced aging, acne, and pigmentation</div>
        <div class="peel-foot">(slightly more aggressive than the other options)</div>
      </div>

      <div class="addons">
        <h3>ADD ONS</h3>
        <div class="addon"><span>Microdermabrasion</span><b>$30</b></div>
        <div class="addon"><span>Radiant Lift &amp; Glow Eye Treatment</span><b>$20</b></div>
        <div class="addon"><span>Hot or Cold Stones</span><b>$15</b></div>
        <div class="addon"><span>Extended Massage</span><b>$15</b></div>
        <div class="addon"><span>Peppermint Scalp Massage</span><b>$15</b></div>
        <div class="addon"><span>Foot Scrub &amp; Massage</span><b>$20</b></div>
        <div class="addon"><span>Aromatherapy</span><b>$10</b></div>
        <div class="addon addon--sub"><span>• Specialty Ampoule</span><b>$15</b></div>
        <div class="addon addon--sub"><span>• Specialty Mask</span><b>$13</b></div>
      </div>
    </div>

    <div class="rates">
      <h2 style="top:8px">EYELASHES</h2>

      <div class="label" style="top:34px">CLASSIC</div>
      <div class="rate" style="top:45px"><span>Full Set</span><span>$175</span></div>
      <div class="rate" style="top:54px"><span>Demi Set</span><span>$110</span></div>
      <div class="rate" style="top:66px"><span>Touch up</span><span>$60</span></div>

      <div class="label" style="top:80px">VOLUME TECHNIQUE</div>
      <div class="rate" style="top:91px"><span>Full Set</span><span>$220</span></div>
      <div class="rate" style="top:100px"><span>Demi Set</span><span>$135</span></div>
      <div class="rate" style="top:112px"><span>Touch up</span><span>$72</span></div>

      <div class="lash-photo" style="top:33px" role="img" aria-label="Close-up photo of eyelash extensions"></div>
      <div class="lash-photo" style="top:62px" role="img" aria-label="Close-up photo of closed eyes with lash extensions"></div>
      <div class="lash-photo" style="top:91px" role="img" aria-label="Close-up photo of volume lash extensions"></div>

      <div class="label" style="top:126px">WAXING</div>
      <div class="rate" style="top:138px"><span>Eyebrows</span><span>$17</span></div>
      <div class="rate" style="top:146.5px"><span>Upper Lip</span><span>$14</span></div>
      <div class="rate" style="top:155px"><span>Chin</span><span>$14</span></div>
      <div class="rate" style="top:163.5px"><span>Sides of face</span><span>$14</span></div>
      <div class="rate" style="top:172px"><span>Bikini</span><span>$27+</span></div>
      <div class="rate" style="top:180.5px"><span>Brazilian</span><span>$55+</span></div>
      <div class="rate" style="top:189px"><span>Underarm</span><span>$22</span></div>
      <div class="rate" style="top:197.5px"><span>Arms Full</span><span>$35 Lower $26</span></div>
      <div class="rate" style="top:206px"><span>Legs Full</span><span>$62 Lower $40</span></div>
      <div class="rate" style="top:214.5px"><span>Chest</span><span>$44</span></div>
      <div class="rate" style="top:223px"><span>Back</span><span>$44</span></div>

      <div class="label" style="top:238px">TINTING</div>
      <div class="rate" style="top:249px"><span>Eyebrows</span><span>$20</span></div>
      <div class="rate" style="top:257.5px"><span>Eyelashes</span><span>$20</span></div>
      <div class="rate" style="top:266px"><span>Both</span><span>$30</span></div>

      <h2 style="top:279px">MASSAGES</h2>
      <div class="massage" style="top:302px">Neck, Back &amp; Head Massage<span><span>30 minutes</span><span>$45</span></span></div>
      <div class="massage" style="top:328px">Aromatherapy Scalp Massage<span><span>10 minutes</span><span>$15</span></span></div>
      <div class="massage" style="top:354px">Foot Massage and Scrub<span><span>15 minutes</span><span>$20</span></span></div>
      <div class="massage" style="top:379px">Headache &amp; Migraine Relief Treatment<span><span>30 minutes</span><span>$45</span></span></div>
      <div class="massage-photo" role="img" aria-label="Soft faded photo of a woman receiving a relaxing massage"></div>
      <p class="massage-note">Relief from headaches caused by stress, tension, hormonal imbalances or sensitivities using cold stones and massaging techniques for the face.</p>
    </div>
  </section>

</div>
</body>
</html>
```